Maple Ridge business card design

Card needs to include the following text/items:
Company Logo
Tobin Marsh
Phone # - 555-318-7642
service@mapleridgelandscaping.example
Lawn & landscape maintenance services

```html
<!DOCTYPE html>
<html lang="en">
<head>
<meta charset="utf-8">
<title>Maple Ridge Landscaping – Business Card</title>
<link rel="stylesheet" href="https://fonts.googleapis.com/css2?family=Cinzel:wght@700&family=Open+Sans:wght@300;700&display=swap">
<style>
  :root {
    --bg: #d1d3d5;
    --forest: #14462a;
    --olive: #7a9228;
    --ink: #231f20;
    --paper: #ffffff;
    --logo-disc: #5f8f3a;
  }
  html, body {
    margin: 0;
    padding: 0;
    width: 1200px;
    height: 1200px;
    overflow: hidden;
    background: var(--bg);
  }
  .card {
    position: absolute;
    left: 250px;
    width: 700px;
    height: 400px;
    background: var(--paper);
    overflow: hidden;
  }
  .card--front { top: 160px; }
  .card--back { top: 641px; }
  .card__shapes {
    position: absolute;
    inset: 0;
    width: 100%;
    height: 100%;
  }
  .shape--forest { fill: var(--forest); }
  .shape--olive { fill: var(--olive); }

  .brand {
    position: absolute;
    left: 0;
    right: 0;
    top: 58px;
    text-align: center;
  }
  .brand__mark {
    display: block;
    width: 190px;
    height: 190px;
    margin: 0 auto;
    border-radius: 50%;
    background: var(--logo-disc);
  }
  .brand__name {
    margin: 14px 0 0;
    font-family: "Cinzel", serif;
    font-weight: 700;
    font-size: 46px;
    line-height: 1;
    color: var(--forest);
  }

  .services {
    position: absolute;
    left: 0;
    right: 0;
    top: 98px;
    text-align: center;
    font-family: "Cinzel", serif;
    font-weight: 700;
  }
  .services__title {
    margin: 0;
    font-size: 47px;
    line-height: 1;
    color: var(--forest);
    letter-spacing: 1px;
  }
  .services__subtitle {
    margin: 6px 0 0;
    font-size: 27px;
    line-height: 1;
    color: var(--ink);
    letter-spacing: 1.5px;
  }
  .divider {
    position: absolute;
    left: 40px;
    width: 619px;
    top: 193px;
    height: 2px;
    background: var(--forest);
  }
  .contact {
    position: absolute;
    left: 40px;
    top: 212px;
    margin: 0;
    padding: 0;
    list-style: none;
    font-family: "Open Sans", sans-serif;
    font-weight: 300;
    font-size: 21px;
    color: var(--ink);
  }
  .contact__item {
    display: flex;
    align-items: center;
    height: 36.5px;
  }
  .contact__icon {
    width: 20px;
    height: 20px;
    margin-right: 13px;
    fill: var(--forest);
    flex: none;
  }
  .person {
    position: absolute;
    right: 40px;
    top: 211px;
    margin: 0;
    font-family: "Open Sans", sans-serif;
    font-weight: 700;
    font-size: 31px;
    line-height: 1.1;
    color: var(--forest);
  }
</style>
</head>
<body>

<section class="card card--front">
  <svg class="card__shapes" viewBox="0 0 1127 643" preserveAspectRatio="none" aria-hidden="true">
    <path class="shape--olive" d="M0,0 L657,0 Q110,110 0,590 Z"/>
    <path class="shape--forest" d="M0,0 L590,0 Q70,140 0,560 Z"/>
    <path class="shape--olive" d="M470,643 Q1060,520 1127,80 L1127,643 Z"/>
    <path class="shape--forest" d="M545,643 Q1080,540 1127,130 L1127,643 Z"/>
  </svg>
  <div class="brand">
    <span class="brand__mark"></span>
    <p class="brand__name">Maple Ridge</p>
  </div>
</section>

<section class="card card--back">
  <svg class="card__shapes" viewBox="0 0 1127 643" preserveAspectRatio="none" aria-hidden="true">
    <path class="shape--olive" d="M0,0 L1127,0 Q563,218 0,0 Z"/>
    <path class="shape--forest" d="M0,0 L1127,0 Q563,190 0,0 Z"/>
    <path class="shape--olive" d="M0,643 Q563,423 1127,643 Z"/>
    <path class="shape--forest" d="M0,643 Q563,457 1127,643 Z"/>
  </svg>

  <div class="services">
    <h1 class="services__title">LAWN &amp; LANDSCAPE</h1>
    <h2 class="services__subtitle">MAINTENANCE SERVICES</h2>
  </div>

  <div class="divider"></div>

  <ul class="contact">
    <li class="contact__item">
      <svg class="contact__icon" viewBox="0 0 24 24" aria-hidden="true"><path d="M6.6 2.5l3 3.6-1.9 2.3c.9 2.6 2.9 5 5.6 6.4l2.1-1.8 3.8 2.8-1.6 3.6C10.4 19.3 4.6 12.4 4.2 3.9z"/></svg>
      <span>555-318-7642</span>
    </li>
    <li class="contact__item">
      <svg class="contact__icon" viewBox="0 0 24 24" aria-hidden="true"><path d="M2 5h20v14H2z M4 7v.4l8 6 8-6V7l-8 6z M4 17h3.5l3-3-6.5-4.8z M20 17h-3.5l-3-3 6.5-4.8z" fill-rule="evenodd"/></svg>
      <span>service@mapleridgelandscaping.example</span>
    </li>
    <li class="contact__item">
      <svg class="contact__icon" viewBox="0 0 24 24" aria-hidden="true"><path fill-rule="evenodd" d="M12 1.5a10.5 10.5 0 1 0 0 21 10.5 10.5 0 0 0 0-21zM3.6 11h3.5c.1-2.4.6-4.5 1.4-6.1A8.5 8.5 0 0 0 3.6 11zm0 2a8.5 8.5 0 0 0 4.9 6.1c-.8-1.6-1.3-3.7-1.4-6.1zm5.5 0c.2 3.8 1.6 6.5 2.9 7.3 1.3-.8 2.7-3.5 2.9-7.3zm5.8 0c-.1 2.4-.6 4.5-1.4 6.1a8.5 8.5 0 0 0 4.9-6.1zm3.5-2a8.5 8.5 0 0 0-4.9-6.1c.8 1.6 1.3 3.7 1.4 6.1zm-5.5 0C12.7 7.2 11.3 4.5 12 3.7c-1.3.8-2.7 3.5-2.9 7.3z"/></svg>
      <span>www.mapleridgelandscaping.example</span>
    </li>
  </ul>

  <p class="person">TOBIN MARSH</p>
</section>

</body>
</html>
```